Lantern Square, Steady Course. (Website Design)

We are launching a new bipartisan civic movement: Lantern Square. Steady Course.
The mission is this: Americans deserve a government that is legally required to serve them honestly.
We are looking for a world-class website designer capable of creating an emotionally powerful, modern, cinematic landing page experience that feels larger than politics.
This is not a campaign website for a political party or candidate. We are not looking for a red, white, and blue page with stripes, or American flags, or stock footage of smiling people in a voting booth. We are looking for an emotional and cinematic experience through and through.
The visual direction should feel:
Historic
Hopeful
American
Emotional
Cinematic
Trustworthy
Timeless
The goal is to make visitors feel that they are witnessing the beginning of something important and want to be part of it in the end.
Primary Objective:
Inspire visitors to participate in a one-minute survey and cast their vote.
The survey itself is extremely short and takes approximately one minute to complete.
Everything on the page should ultimately guide visitors toward this action while creating enough curiosity, trust, emotional engagement, and excitement that they feel compelled to take part in the movement.
Audience:
The audience is ordinary Americans across the political spectrum: Democrats, Republicans, Independents.
The design should feel unifying and welcoming.
It should avoid looking partisan, ideological, activist, or government-issued.
Creative Freedom:
We are intentionally giving designers substantial creative freedom.
We are not looking for someone to simply arrange content into predefined sections.
Instead, we are looking for a designer who can think strategically about user experience and persuasion.
The ideal design is as minimal as possible, but you may always:
Use as many sections as you believe are necessary.
Use as many images as you believe are necessary.
Include storytelling elements.
Include data visualizations.
Include timelines.
Include videos.
Include animations.
Include or exclude sections as you see fit.
Reorganize the flow entirely.
We uploaded some files containing text and section suggestions. You don’t have to use them.
We also uploaded some images to convey the general feel we’re looking for.
We are much more interested in the effectiveness of the overall experience than in any specific layout.
What success looks like:
Think outside the box.
Please do not create another generic political website. We have already explored those approaches.
We are looking for something different.
The winning design will be the one that most effectively guides visitors from curiosity to belief to participation.
When a visitor reaches the end of the experience, they should feel:
This is bigger than politics.
This is something I can support regardless of party.
This feels credible.
This feels hopeful.
I want to be part of this.
Use the survey results, the research findings, the principles, the storytelling, or any other elements you believe will help build trust and inspire participation.
Don't just impress us with flashy visuals. Impress us with a website experience that inspires people to become part of the movement and cast their vote.
The final call-to-action should feel like the natural conclusion of the journey, not a request for engagement.
Our goal is not simply to inform visitors. Our goal is to inspire them to cast their vote.
Prioritize emotional impact, storytelling, clarity, and persuasion over decorative design elements.
Final words:
Design a website experience that successfully inspires visitors to take the survey and cast their vote.
Think like a storyteller, not just a designer.
Thank you for your interest in the project.
Best of luck.

```html
<!DOCTYPE html>
<html lang="en">
<head>
<meta charset="utf-8">
<title>Lantern Square. Steady Course.</title>
<link rel="stylesheet" href="https://fonts.googleapis.com/css2?family=Inter:wght@400;500;600&family=Playfair+Display:ital,wght@0,400;0,500;1,400&display=swap">
<style>
:root{
  --gold:#c9a54a;
  --gold-soft:#e3c98a;
  --navy:#1e2a44;
  --navy-deep:#121a2e;
  --cream:#f3efe5;
  --ink:#1d2230;
  --muted:#6b6f78;
  --white:#ffffff;
  --line:#d9d5cc;
}
*{box-sizing:border-box;margin:0;padding:0}
html,body{width:1200px;height:3447px;overflow:hidden}
body{font-family:"Inter",sans-serif;color:var(--ink);background:var(--navy-deep)}
section,footer{position:relative;width:1200px;overflow:hidden}
.abs{position:absolute}
.center{left:0;right:0;text-align:center}
.bg{position:absolute;inset:0}
.line{display:block;white-space:nowrap}

/* hero */
.hero{height:573px}
.hero .bg{background:linear-gradient(180deg,#4f5a78 0%,#6b6c7f 28%,#7a6d6c 40%,#4a5370 60%,#2e3a55 100%)}
.brand{left:28px;top:24px;color:var(--white);font-family:"Playfair Display",serif;font-size:17px}
.nav-cta{left:1013px;top:16px;width:158px;height:35px;border-radius:18px;background:var(--gold-soft);color:var(--ink);font-size:11.5px;font-weight:600;letter-spacing:1.2px;display:flex;align-items:center;justify-content:center}
.badge{left:473px;top:84px;width:254px;height:28px;border:1px solid rgba(201,165,74,.6);border-radius:14px;color:var(--gold);font-size:10px;font-weight:600;letter-spacing:1.1px;display:flex;align-items:center;justify-content:center}
.hero-title{top:140px;color:var(--white);font-family:"Playfair Display",serif;font-size:84px;line-height:86px;font-weight:500}
.hero-title em{color:var(--gold-soft);font-weight:400}
.hero-sub{top:334px;color:var(--white);font-size:18px;line-height:31px}
.btn{display:flex;align-items:center;justify-content:center;gap:12px;background:var(--gold);color:var(--ink);border-radius:32px;font-weight:500}
.hero .btn{left:499px;top:431px;width:202px;height:57px;font-size:14px}
.scroll{left:0;right:0;top:480px;text-align:center;color:rgba(255,255,255,.35);font-size:7px;letter-spacing:1.5px}
.scroll-line{left:621px;top:506px;width:1px;height:18px;background:rgba(255,255,255,.4)}

/* broken */
.broken{height:968px}
.broken .bg{background:linear-gradient(180deg,#2b3550 0%,#3d4663 38%,#3a4462 55%,#27324e 75%,#1f2c4c 100%)}
.h2-light{color:var(--white);font-family:"Playfair Display",serif}
.broken h2{top:8px;font-size:41px;line-height:56px;font-weight:400;letter-spacing:-0.3px}
.broken .lede{top:130px;color:var(--white);font-size:16px;line-height:29px}
.stat-card{top:259px;width:381px;height:209px;background:rgba(70,82,112,.5);border:1px solid rgba(255,255,255,.12);text-align:center;padding:34px 28px 0;color:var(--white)}
.stat-card .num{font-family:"Playfair Display",serif;color:var(--gold);font-size:44px;line-height:48px}
.stat-card h3{font-size:14.5px;font-weight:600;margin-top:2px}
.stat-card p{font-size:12px;line-height:21px;color:rgba(255,255,255,.78);margin-top:8px}
.quote{top:478px;color:var(--white);font-family:"Playfair Display",serif;font-style:italic;font-size:40px;line-height:55px}
.cite{top:722px;color:var(--gold);font-size:12.5px;font-weight:500}
.mini{top:783px;width:180px;text-align:center;color:var(--white)}
.mini .num{font-family:"Playfair Display",serif;color:var(--gold);font-size:62px;line-height:66px}
.mini p{font-size:12px;line-height:19px}
.stars{top:940px;color:var(--gold);font-size:16px;letter-spacing:66px;padding-left:66px}

/* beliefs */
.beliefs{height:351px;background:var(--cream)}
.beliefs h2{top:12px;font-family:"Playfair Display",serif;font-size:44px;font-weight:400}
.beliefs .sub{top:83px;color:var(--muted);font-size:15px}
.belief{top:154px;width:376px;height:197px;background:var(--white);border-left:3px solid var(--gold);padding:34px 28px 0 28px}
.belief h3{font-family:"Playfair Display",serif;font-weight:400;font-size:20px}
.belief p{font-size:12.5px;line-height:22px;color:var(--muted);margin-top:10px}

/* imagine */
.imagine{height:444px}
.imagine .bg{background:linear-gradient(180deg,#2a3350 0%,#2d3a52 45%,#344437 75%,#2b3a32 100%)}
.imagine h2{top:6px;font-size:44px;font-weight:400}
.imagine h2 em{color:var(--gold-soft)}
.imagine .lede{top:80px;color:var(--white);font-size:15px;line-height:26.5px}
.feature{top:199px;width:278px;height:245px;background:rgba(55,68,84,.55);border:1px solid rgba(255,255,255,.12);text-align:center;color:var(--white);padding:28px 26px 0}
.icon{width:42px;height:42px;margin:0 auto;display:block}
.feature h3{font-family:"Playfair Display",serif;font-weight:500;font-size:16.5px;margin-top:16px}
.feature p{font-size:15px;line-height:27px;margin-top:18px;color:rgba(255,255,255,.9)}

/* survey */
.survey{height:581px;background:var(--cream)}
.survey h2{top:10px;font-family:"Playfair Display",serif;font-size:43px;font-weight:400}
.survey .sub{top:72px;color:var(--muted);font-size:15px;line-height:24px}
.survey-card{left:333px;top:154px;width:534px;height:427px;background:var(--white);border-top:3px solid var(--gold-soft);padding:38px 36px 0}
.steps{display:flex;justify-content:space-between;align-items:center}
.dots{display:flex;gap:8px}
.dot{width:6px;height:6px;border-radius:50%;background:var(--line)}
.dot.on{background:var(--gold)}
.count{font-size:10.5px;color:var(--muted)}
.question{font-size:16.5px;line-height:26px;margin-top:36px;font-weight:500}
.option{height:47px;border:1px solid var(--line);margin-top:12px;font-size:13.5px;padding:0 18px;display:flex;align-items:center}
.question + .option{margin-top:24px}

/* final */
.final{height:439px}
.final .bg{background:linear-gradient(180deg,#2c3450 0%,#3b3d55 40%,#4a4248 70%,#3a3530 100%)}
.final h2{top:8px;font-size:56px;line-height:60px;font-weight:500}
.final h2 em{color:var(--gold-soft);font-weight:400}
.final .lede{top:204px;color:var(--white);font-size:15px;line-height:26px}
.final .btn{left:467px;top:307px;width:266px;height:58px;font-size:16px}
.fine{top:388px;color:rgba(255,255,255,.45);font-size:11px;letter-spacing:1.4px}

footer{height:91px;background:var(--navy-deep)}
footer p{top:38px;color:rgba(255,255,255,.4);font-size:11px}
footer a{color:var(--gold);text-decoration:none}
</style>
</head>
<body>

<section class="hero">
  <div class="bg" role="img" aria-label="Mountain range above a sea of clouds at sunset"></div>
  <div class="abs brand">Lantern Square. Steady Course.</div>
  <div class="abs nav-cta">TAKE THE SURVEY</div>
  <div class="abs badge">A NEW BIPARTISAN CIVIC MOVEMENT</div>
  <h1 class="abs center hero-title">Lantern Square.<br><em>Steady Course.</em></h1>
  <p class="abs center hero-sub">Americans deserve a government that is legally required to serve<br>them honestly. Not parties. Not donors. Not itself. <em>Us.</em></p>
  <a class="abs btn">Cast Your Vote <span>&#8594;</span></a>
  <div class="abs scroll">SCROLL</div>
  <div class="abs scroll-line"></div>
</section>

<section class="broken">
  <div class="bg" role="img" aria-label="Group of people seen from behind, arm in arm, looking toward a city skyline across the water"></div>
  <h2 class="abs center h2-light"><span class="line">Most Americans agree on what's broken — even if we disagree</span><span class="line">on everything else.</span></h2>
  <p class="abs center lede">For decades, our government has drifted away from the people it was designed<br>to serve. It answers to lobbyists, party machinery, and its own preservation.<br>Across every demographic, every party, every region — Americans feel it.</p>
  <div class="abs stat-card" style="left:0"><div class="num">78%</div><h3>Distrust</h3><p>of Americans say they trust the government only some or none of the time. The highest level in modern history.</p></div>
  <div class="abs stat-card" style="left:409px"><div class="num">82%</div><h3>Common Ground</h3><p>of Democrats and Republicans agree the government was designed to serve the people — and has failed at that mission.</p></div>
  <div class="abs stat-card" style="left:819px"><div class="num">91%</div><h3>Demand for Honesty</h3><p>of Americans believe officials should be legally required to tell the truth. This is not left or right. It is the baseline.</p></div>
  <blockquote class="abs center quote"><span class="line">"The people are the only legitimate source</span><span class="line">of power, and it is from them that the</span><span class="line">constitutional charter derives its</span><span class="line">authority."</span></blockquote>
  <div class="abs center cite">— The Federalist Papers</div>
  <div class="abs mini" style="left:278px"><div class="num">87%</div><p>Bipartisan support for legal honesty standard in government</p></div>
  <div class="abs mini" style="left:509px"><div class="num">73%</div><p>Feel personally let down by government's lack of transparency</p></div>
  <div class="abs mini" style="left:741px"><div class="num">94%</div><p>Say honesty matters more than party affiliation</p></div>
  <div class="abs center stars">&#10022;&#10022;&#10022;</div>
</section>

<section class="beliefs">
  <h2 class="abs center">What We Believe</h2>
  <p class="abs center sub">Three principles. No party affiliation. The baseline of a functioning democracy.</p>
  <div class="abs belief" style="left:0"><h3>Honesty</h3><p>Government officials must be legally required to tell the truth to the people they serve. Transparency is not aspirational — it must be the law.</p></div>
  <div class="abs belief" style="left:412px"><h3>Service</h3><p>Government exists to serve every American equally, regardless of party, wealth, or influence. When it serves itself, it has lost its mandate.</p></div>
  <div class="abs belief" style="left:824px"><h3>Accountability</h3><p>Citizens have the right to know how their government operates, where their money goes, and who is making decisions on their behalf.</p></div>
</section>

<section class="imagine">
  <div class="bg" role="img" aria-label="Rolling green countryside under a dusky sky"></div>
  <h2 class="abs center h2-light">Imagine a government that <em>has to</em> tell you the truth.</h2>
  <p class="abs center lede">Not a perfect government. Not one everyone agrees with. But one that is<br>legally bound to serve you honestly. That is not a partisan goal. That is<br>an American one.</p>
  <div class="abs feature" style="left:0">
    <svg class="icon" viewBox="0 0 42 42"><circle cx="21" cy="21" r="20" fill="none" stroke="#c9a54a"/><path d="M21 13v16M17 19h8" stroke="#c9a54a" stroke-width="1.4"/></svg>
    <h3>Clear Information</h3><p>Policies explained in plain language, not legal loopholes</p></div>
  <div class="abs feature" style="left:306px">
    <svg class="icon" viewBox="0 0 42 42"><circle cx="21" cy="21" r="20" fill="none" stroke="#c9a54a"/><path d="M21 16l5 5-5 5-5-5z" fill="none" stroke="#c9a54a" stroke-width="1.4"/></svg>
    <h3>Open Budgets</h3><p>Every dollar tracked and accessible to every citizen</p></div>
  <div class="abs feature" style="left:614px">
    <svg class="icon" viewBox="0 0 42 42"><circle cx="21" cy="21" r="20" fill="none" stroke="#c9a54a"/><circle cx="21" cy="21" r="6" fill="none" stroke="#c9a54a" stroke-width="1.4"/><circle cx="21" cy="21" r="2.5" fill="#c9a54a"/></svg>
    <h3>Direct Representation</h3><p>Leaders who answer to people, not party donors</p></div>
  <div class="abs feature" style="left:922px">
    <svg class="icon" viewBox="0 0 42 42"><circle cx="21" cy="21" r="20" fill="none" stroke="#c9a54a"/><rect x="14.5" y="14.5" width="13" height="13" fill="none" stroke="#c9a54a" stroke-width="1.4"/><path d="M21 14.5v13M14.5 21h13" stroke="#c9a54a" stroke-width="1.2"/></svg>
    <h3>Public Trust</h3><p>A government that earns confidence through accountability</p></div>
</section>

<section class="survey">
  <h2 class="abs center">One minute. One voice.</h2>
  <p class="abs center sub">The first step toward change. A short survey that tells leaders<br>what Americans want — not what pundits assume.</p>
  <div class="abs survey-card">
    <div class="steps"><div class="dots"><span class="dot on"></span><span class="dot"></span><span class="dot"></span><span class="dot"></span></div><span class="count">1 of 4</span></div>
    <p class="question">Should the government be legally required to tell the truth to citizens?</p>
    <div class="option">Yes — absolutely</div>
    <div class="option">Yes, with reasonable exceptions</div>
    <div class="option">No</div>
    <div class="option">Not sure</div>
  </div>
</section>

<section class="final">
  <div class="bg" role="img" aria-label="Open farmland at dusk with distant trees on the horizon"></div>
  <h2 class="abs center h2-light">This is bigger than politics.<br>This is <em>Lantern Square.</em><br><em>Steady Course.</em></h2>
  <p class="abs center lede">We are not asking for money. We are not asking for your party.<br>We are asking for your voice. One minute. One vote. Be part of<br>the first step toward a government that serves us all.</p>
  <a class="abs btn">Cast Your Vote Now <span>&#8594;</span></a>
  <p class="abs center fine">NO SIGN-UP REQUIRED. NO EMAIL. JUST ONE MINUTE OF YOUR TIME.</p>
</section>

<footer>
  <p class="abs center">Lantern Square. Steady Course. — A bipartisan civic movement. <a>Learn more</a></p>
</footer>

</body>
</html>
```